Vela Link and Wire post card design

We need a postcard to hand out to prospective clients detailing what we do with contact details kept to just a mobile phone number.
Vela Link and Wire is a communications networking company specialising in computer cabling, phone cabling, fibre optics, CCTV, particularly for small business. We offer licenced technicians with over 20 years experience in this field. We service greater Brisbane. Designs that incorporate colours from our logo would be great and that is similar to our business card.
Communications

```html
<!DOCTYPE html>
<html lang="en">
<head>
<meta charset="utf-8">
<title>Vela Link and Wire – Postcard</title>
<link href="https://fonts.googleapis.com/css2?family=Arimo:ital,wght@0,700;1,700&family=Share+Tech+Mono&display=swap" rel="stylesheet">
<style>
  :root {
    --page: #d9d9d9;
    --card-black: #050805;
    --card-paper: #e8e8e6;
    --brand-green: #3f9a2e;
    --band-olive: #a7b02a;
    --band-line: #2f8f2a;
    --band-text: #e6d84a;
    --white: #ffffff;
    --address-grey: #8a8a88;
    --stamp-grey: #a9b2a6;
  }
  * { box-sizing: border-box; margin: 0; padding: 0; }
  html, body { width: 1200px; height: 884px; overflow: hidden; background: var(--page); }
  body { position: relative; font-family: "Arimo", Arial, sans-serif; }

  .postcard {
    position: absolute; top: 262px; width: 540px; height: 360px;
    box-shadow: 0 2px 8px rgba(0,0,0,.25); overflow: hidden;
  }
  .postcard--front { left: 30px; background: var(--card-black); }
  .postcard--back { left: 630px; background: var(--card-paper); }

  /* front */
  .fibre-visual {
    position: absolute; inset: 40px 0 60px 0;
    background:
      radial-gradient(ellipse at 30% 85%, rgba(60,200,80,.55), transparent 55%),
      radial-gradient(ellipse at 75% 80%, rgba(40,170,60,.5), transparent 55%),
      linear-gradient(180deg, var(--card-black) 0%, #062a0c 60%, #0b4a16 100%);
  }
  .headline {
    position: absolute; left: 56px; top: 30px;
    color: var(--white); font-style: italic; font-size: 14px; letter-spacing: .2px;
  }
  .brand {
    position: absolute; display: flex; align-items: center; gap: 6px;
    color: var(--brand-green); font-weight: 700;
  }
  .brand__dot { border-radius: 50%; background: var(--band-olive); }
  .postcard--front .brand { right: 22px; top: 28px; font-size: 14px; }
  .postcard--front .brand__dot { width: 16px; height: 16px; }
  .tagline {
    position: absolute; right: 30px; top: 76px;
    color: var(--white); font-style: italic; font-size: 9.5px;
  }
  .service-band {
    position: absolute; left: 0; right: 0; height: 20px;
    border: 1px solid var(--band-line); border-left: 0; border-right: 0;
    background: rgba(0,0,0,.85);
    display: flex; align-items: center; padding-left: 12px; gap: 16px;
    font-family: "Share Tech Mono", monospace; font-size: 11.5px; letter-spacing: 1.2px;
    color: var(--band-text);
  }
  .service-band--one { top: 240px; }
  .service-band--two { top: 266px; }
  .contact-band {
    position: absolute; left: 0; right: 0; top: 294px; height: 22px;
    border-top: 1px solid var(--band-line); border-bottom: 1px solid var(--band-line);
    background: rgba(0,0,0,.9); color: var(--white);
    display: flex; align-items: center; gap: 20px; padding-left: 12px;
    font-size: 9.5px;
  }

  /* back */
  .postcard--back .brand { left: 22px; top: 22px; font-size: 20px; }
  .postcard--back .brand__dot { width: 22px; height: 22px; }
  .stamp-box { position: absolute; right: 14px; top: 10px; }
  .services-title {
    position: absolute; left: 0; top: 100px; width: 178px; height: 32px;
    background: var(--band-olive); color: var(--white);
    font-style: italic; font-size: 18px; padding: 6px 0 0 26px;
  }
  .service-list {
    position: absolute; left: 26px; top: 145px; list-style: none;
    color: var(--brand-green); font-style: italic; font-size: 14.5px; line-height: 18.6px;
  }
  .recipient {
    position: absolute; left: 236px; top: 168px;
    font-family: "Share Tech Mono", monospace; font-size: 13px; line-height: 14.5px;
    letter-spacing: 1.5px; color: var(--address-grey); font-style: normal;
  }
</style>
</head>
<body>
  <section class="postcard postcard--front">
    <div class="fibre-visual" role="img" aria-label="Photograph of glowing green fibre optic strands on black"></div>
    <p class="headline">SPECIALISING IN SMALL BUSINESS</p>
    <div class="brand"><span class="brand__dot"></span>Vela Link and Wire</div>
    <p class="tagline">Technicians with over 20 years experience!</p>
    <div class="service-band service-band--one">
      <span>Communications</span><span>WiFi</span><span>Telephone faults/relocation</span>
    </div>
    <div class="service-band service-band--two">
      <span>Computer cabling</span><span>CCTV</span><span>Fibre optics</span><span>Phone cabling</span>
    </div>
    <div class="contact-band">
      <span>Contact us : ben@velalinkwire.com</span><span>0412 555 018</span><span>www.velalinkwire.com</span>
    </div>
  </section>

  <section class="postcard postcard--back">
    <div class="brand"><span class="brand__dot"></span>Vela Link and Wire</div>
    <svg class="stamp-box" width="100" height="66" viewBox="0 0 100 66">
      <rect x="2" y="2" width="96" height="62" fill="none" stroke="var(--stamp-grey)" stroke-width="3" stroke-dasharray="14 8"/>
    </svg>
    <h2 class="services-title">Our Services:</h2>
    <ul class="service-list">
      <li>WiFi</li>
      <li>CCTV</li>
      <li>Fibre optics</li>
      <li>Phone cabling</li>
      <li>Communications</li>
      <li>Computer cabling</li>
      <li>Office network relocations</li>
      <li>Telephone faults/relocations</li>
    </ul>
    <address class="recipient">
      Mara Lowe<br>
      58 Sample Street<br>
      Westbrook City,Ny<br>
      40217-5580
    </address>
  </section>
</body>
</html>
```